Label for Refill packaging eco-conscious beauty brand

We need a label for our refill pouch. Velvet Harbor is an unscented conditioner formulated using the finest healthy & pure ingredients, free of chemicals and harmful toxins. As a minimalist beauty brand we are proud to be certified with TPL, VerdaSeal and Silver Fawn.

We already have the pouches and an exciting label for our regular bottles.
We choose a kraft brown packing for the refill pouch and would like something minimalist but elegant for the label.

```html
<!DOCTYPE html>
<html lang="en">
<head>
<meta charset="utf-8">
<title>LUMEN Sorrel – Velvet Harbor refill label</title>
<link href="https://fonts.googleapis.com/css2?family=Cabin:wght@400;500&display=swap" rel="stylesheet">
<style>
  :root {
    --backdrop: #e8c5bf;
    --label-teal: #1e6869;
    --sage: #9cc5b3;
    --sage-soft: #a9cfbf;
    --white: #ffffff;
  }
  * { box-sizing: border-box; margin: 0; padding: 0; }
  html, body {
    width: 1200px;
    height: 848px;
    overflow: hidden;
    background: var(--backdrop);
    font-family: "Cabin", sans-serif;
  }
  .canvas {
    position: relative;
    width: 1200px;
    height: 848px;
  }
  .label {
    position: absolute;
    left: 385px;
    top: 44px;
    width: 430px;
    height: 760px;
    background: var(--label-teal);
    text-align: center;
    color: var(--sage-soft);
  }
  .brand-tile {
    position: absolute;
    left: 152px;
    top: 127px;
    width: 125px;
    height: 212px;
    background: var(--sage);
    display: flex;
    align-items: flex-end;
    justify-content: center;
    padding-bottom: 24px;
  }
  .brand-name {
    color: var(--white);
    font-weight: 500;
    font-size: 25px;
    line-height: 1.22;
    letter-spacing: 0.5px;
  }
  .product-name {
    position: absolute;
    top: 357px;
    left: 0;
    width: 100%;
    font-weight: 500;
    font-size: 26px;
    line-height: 1.0;
  }
  .product-description {
    position: absolute;
    top: 437px;
    left: 0;
    width: 100%;
    font-size: 13.2px;
    line-height: 1.28;
  }
  .divider {
    position: absolute;
    top: 508px;
    left: 145px;
    width: 140px;
    height: 1px;
    background: var(--sage-soft);
  }
  .certification-note {
    position: absolute;
    top: 538px;
    left: 143px;
    width: 144px;
    font-size: 8.6px;
    line-height: 1.55;
    text-align: justify;
    text-align-last: justify;
  }
  .volume {
    position: absolute;
    top: 620px;
    left: 0;
    width: 100%;
    font-size: 10.5px;
    letter-spacing: 0.3px;
  }
</style>
</head>
<body>
  <main class="canvas">
    <section class="label">
      <div class="brand-tile">
        <p class="brand-name">LUMEN<br>Sorrel</p>
      </div>
      <h1 class="product-name">Velvet<br>Harbor</h1>
      <p class="product-description">an unscented conditioner formulated<br>using the finest healthy &amp; pure ingredients,<br>free of chemicals &amp; harmful toxins.</p>
      <div class="divider"></div>
      <p class="certification-note">As a minimalist beauty brand we are proud to be certified with TPL, VerdaSeal &amp; Silver Fawn.</p>
      <p class="volume">8 fl. oz ℮ 238ml</p>
    </section>
  </main>
</body>
</html>
```